Business card design for immigration consulting business

We need business card design for a company called T&R Migration Advisors Inc. This is a boutique immigration consulting and foreign recruitment agency owned and managed by two partners.
The business card will be used by partners \ owners of the business. The best way to describe the business would be committed to client, passionate about providing top-notch services, engaging, competent, professional

Target Market(s)

We work with individuals in and outside of Canada who need immigration advise as well as Canadian businesses looking to hire or sponsor foreign workers to Canada

Industry/Entity Type

Consulting

Contact Information for Business Card

The business card should have a standard size and horizontal lay-out

Font styles to use
Serif

Colors
f04a50
ec1f27
cbcbcb
dbdbdb

Requirements
Must have
• The business card mush have our logo, name of the company first and last name of the partner, position, phone, cell, fax, e-mail, skype, web-site
• Our first choice would a classic design with minimalist looks and elegant fonts and colors, but we are open minded to any creative ideas too
Nice to have
• On the other side it may have the description of the company: Immigration and Foreign Recruitment Services
• We're considering using stamping \ lettering on our business cards
• It would be nice if the business card would have white space, in case someone would like to make notes on it.
• One (back side) side of the business card can be all red with white logo
Should not have
• We do not want to have our pictures on the business card
• We do no want to have Canadian maple leaf on the business card as we already have one in our logo

```html
<!DOCTYPE html>
<html lang="en">
<head>
<meta charset="utf-8">
<title>T&amp;R Migration Advisors – Business Card</title>
<link href="https://fonts.googleapis.com/css2?family=Tinos:wght@400;700&display=swap" rel="stylesheet">
<style>
  :root {
    --brand-red: #ec1f27;
    --accent-red: #f04a50;
    --ink-grey: #6b6b6b;
    --text-grey: #555555;
    --rule-grey: #9a9a9a;
    --paper: #ffffff;
    --paper-shade: #f1f1f1;
    --backdrop: #e6e3de;
    --serif: "Tinos", "Times New Roman", serif;
  }
  * { box-sizing: border-box; margin: 0; padding: 0; }
  html, body { width: 900px; height: 1200px; overflow: hidden; }
  body { background: var(--backdrop); font-family: var(--serif); position: relative; }

  .card { position: absolute; width: 724px; height: 422px; left: 86px; }
  .card--front {
    top: 145px;
    background: linear-gradient(160deg, var(--paper) 55%, var(--paper-shade) 100%);
  }
  .card--back { top: 637px; background: var(--brand-red); color: #fff; text-align: center; }

  .brand-name {
    position: absolute;
    font-weight: 400;
    line-height: 1;
    white-space: nowrap;
  }
  .card--front .brand-name { left: 55px; top: 92px; font-size: 52px; color: var(--ink-grey); }
  .card--back .brand-name { left: 0; right: 0; top: 178px; font-size: 60px; color: #fff; }

  .person { position: absolute; right: 56px; top: 176px; text-align: right; }
  .person__name { font-size: 29px; font-weight: 700; color: var(--ink-grey); }
  .person__role { font-size: 18.5px; color: var(--brand-red); margin-top: 4px; }

  .divider { position: absolute; left: 0; right: 0; top: 262px; height: 2px; background: var(--rule-grey); }

  .contacts { position: absolute; top: 287px; list-style: none; font-size: 16.5px; color: var(--text-grey); }
  .contacts li { display: flex; align-items: center; height: 25px; gap: 9px; }
  .contacts--left { left: 55px; }
  .contacts--right { right: 56px; }
  .contacts--right li { justify-content: flex-end; }
  .icon { width: 21px; height: 21px; flex: none; }

  .tagline { position: absolute; left: 0; right: 0; top: 360px; font-size: 22px; }
</style>
</head>
<body>
  <section class="card card--front" aria-label="Business card front">
    <p class="brand-name">T&amp;R Migration</p>
    <div class="person">
      <p class="person__name">Daniel Hartwell</p>
      <p class="person__role">Managing Director</p>
    </div>
    <div class="divider"></div>
    <ul class="contacts contacts--left">
      <li>
        <svg class="icon" viewBox="0 0 20 20" aria-hidden="true"><circle cx="10" cy="10" r="10" fill="var(--brand-red)"/><path d="M6.3 5.2l1.8-.4 1 2.4-1.2.9a6 6 0 0 0 3 3l.9-1.2 2.4 1-.4 1.8c-4 .5-8-3.5-7.5-7.5z" fill="#fff"/></svg>
        <span>+416 555 0142</span>
      </li>
      <li>
        <svg class="icon" viewBox="0 0 20 20" aria-hidden="true"><circle cx="10" cy="10" r="10" fill="var(--brand-red)"/><rect x="6.8" y="4.6" width="6.4" height="10.8" rx="1" fill="none" stroke="#fff" stroke-width="1.4"/><circle cx="10" cy="13.4" r=".7" fill="#fff"/></svg>
        <span>+647 555 0187</span>
      </li>
      <li>
        <svg class="icon" viewBox="0 0 20 20" aria-hidden="true"><circle cx="10" cy="10" r="10" fill="var(--brand-red)"/><rect x="7" y="5" width="6" height="3" fill="#fff"/><rect x="5" y="8.4" width="10" height="4.6" rx=".8" fill="#fff"/><rect x="7" y="11.6" width="6" height="3.4" fill="#fff" stroke="var(--brand-red)" stroke-width=".8"/></svg>
        <span>+416 555 0199</span>
      </li>
    </ul>
    <ul class="contacts contacts--right">
      <li>
        <span>info@trmigration.ca</span>
        <svg class="icon" viewBox="0 0 20 20" aria-hidden="true"><circle cx="10" cy="10" r="10" fill="var(--brand-red)"/><rect x="5" y="6.5" width="10" height="7" fill="#fff"/><path d="M5 6.8l5 4 5-4" fill="none" stroke="var(--brand-red)" stroke-width="1"/></svg>
      </li>
      <li>
        <span>www.trmigration.ca</span>
        <svg class="icon" viewBox="0 0 20 20" aria-hidden="true"><circle cx="10" cy="10" r="10" fill="var(--brand-red)"/><g fill="none" stroke="#fff" stroke-width="1.1"><circle cx="10" cy="10" r="5"/><ellipse cx="10" cy="10" rx="2.2" ry="5"/><path d="M5 10h10M6 7.3h8M6 12.7h8"/></g></svg>
      </li>
      <li>
        <span>trmigration</span>
        <svg class="icon" viewBox="0 0 20 20" aria-hidden="true"><circle cx="10" cy="10" r="10" fill="var(--brand-red)"/><path d="M5.2 6.2h9.6v6.2H9.2l-2.6 2.2v-2.2H5.2z" fill="#fff"/></svg>
      </li>
    </ul>
  </section>

  <section class="card card--back" aria-label="Business card back">
    <p class="brand-name">T&amp;R Migration</p>
    <p class="tagline">Immigration and Foreign Recruitment Services</p>
  </section>
</body>
</html>
```